Sparrowgate Petals Website v.1 - attract floral shop franchisees

I need a simple information website for my new business. We are a franchisor of flower shops. The overall purpose of the website is to promote the company and the service, especially to potential franchisees and retailers. Only about 4 pages are required including homepage, About, For Supermarkets, For Franchisees, and Contact. No special functions are required except the site will have two separate inquiry forms that must be filled out online and submitted via automated email. Similarly, an email form should be linked from the Contact page. I have a logo and business cards designed by ArtQuarry, and I would like the site to have a consistent color scheme and style. The key to design will be to express the joy and love associated with flowers and floral bouquets.
IMPORTANT - I will be exporting the website design to Wordpress CMS in a site hosted by HostNimbus. For smooth integration into WordPress hosted by HostNimbus, the designer should build the site using a WordPress-friendly format. Ideally, they should use HTML, CSS, and PHP. Creating a custom theme or using a page builder that exports to WordPress-compatible files is best. This ensures the site can be easily imported and managed within WordPress.

Target Market(s)

Potential franchisees (existing florists or creative types who might like to own a floral business) and supermarkets who might want us to run their floral department

Industry/Entity Type

Floral retailing

Requirements
Must have
• A brand theme that is beautiful, consistent throughout and builds on the logo design
Nice to have
• Show gender and ethnic diversity in customers and florists. Pictures of happy florists (for franchisees) and pictures of amazing floral department displays (for supermarkets)

```html
<!DOCTYPE html>
<html lang="en">
<head>
<meta charset="utf-8">
<title>Sparrowgate Petals</title>
<link href="https://fonts.googleapis.com/css2?family=Great+Vibes&family=Inter:wght@400;500;600;700&display=swap" rel="stylesheet">
<style>
:root{
  --green:#0b8a3e;
  --orange:#f09c20;
  --ink:#1b1b1b;
  --body:#5a5a5a;
  --white:#ffffff;
  --footer:#0e0e0e;
}
*{margin:0;padding:0;box-sizing:border-box}
html,body{width:1200px;height:2778px;overflow:hidden;background:var(--white)}
body{position:relative;font-family:'Inter',sans-serif;color:var(--ink)}
.abs{position:absolute}
.script{font-family:'Great Vibes',cursive;font-weight:400;color:var(--ink)}

/* top bar */
.topbar{left:528px;top:0;width:672px;height:27px;background:var(--green);border-radius:0 0 0 16px;color:var(--white);font-size:13px;display:flex;align-items:center}
.topbar .social{display:flex;gap:18px;padding-left:30px;width:150px}
.topbar .social span{width:10px;height:10px;border-radius:2px;background:var(--white);display:block}
.topbar .item{display:flex;align-items:center;gap:7px;padding:0 16px;border-left:1px solid rgba(255,255,255,.35);height:27px}
.topbar svg{fill:var(--orange)}

.brand{display:flex;align-items:center;gap:8px}
.brand .dot{width:22px;height:22px;border-radius:50%;background:var(--green)}
.brand .name{font-weight:600;color:var(--orange);font-size:19px;letter-spacing:.2px}

.nav a{position:absolute;top:55px;font-size:14px;font-weight:500;color:var(--ink);text-decoration:none;letter-spacing:.2px}

/* hero */
.hero{left:0;top:94px;width:1200px;height:626px;background:linear-gradient(180deg,#3d7fc6 0%,#8dbfe6 30%,#b8d48e 58%,#5d9a33 75%,#4e8a2a 100%)}
.hero-title{left:142px;top:188px;font-size:62px;line-height:1}
.hero-text{left:142px;top:266px;width:480px;font-size:15.5px;line-height:26px;color:#111}
.btn{position:absolute;display:flex;align-items:center;gap:9px;background:var(--orange);color:var(--white);font-weight:700;border-radius:26px 4px 26px 4px;text-decoration:none}
.btn svg{fill:var(--white)}

/* sections */
.photo{background:linear-gradient(160deg,#d9cdb8,#9a8a6e 55%,#5f6b3f)}
.title{font-size:52px;line-height:1}
.rule{height:4px;width:108px;background:var(--green);border-radius:2px}
.para{font-size:13px;line-height:25px;color:var(--body);text-align:justify}
.para p{margin-bottom:4px}
.subhead{font-size:14px;font-weight:500;color:var(--ink)}
.ticks{list-style:none;font-size:11.5px;color:var(--body)}
.ticks li{display:flex;align-items:center;gap:8px;height:29px}
.ticks svg{flex:none}
.ornament{background:radial-gradient(circle,#fbefcf 0%,rgba(251,239,207,0) 70%)}

/* footer */
.footer-contact{left:0;top:2610px;width:1200px;display:flex;justify-content:center;align-items:center;gap:26px;color:var(--white);font-size:15px}
.footer-contact .sep{color:var(--white)}
.footer-contact .ci{display:flex;align-items:center;gap:9px}
.footer-contact svg{fill:var(--orange)}
.divider{left:200px;width:810px;height:1px;background:rgba(255,255,255,.18)}
.footer-nav{left:0;top:2674px;width:1200px;display:flex;justify-content:center;gap:30px;color:var(--white);font-size:14.5px;font-weight:600}
.copyright{left:0;top:2742px;width:1200px;text-align:center;color:var(--white);font-size:13px}
</style>
</head>
<body>

<!-- header -->
<div class="abs topbar">
  <div class="social"><span></span><span></span><span></span><span></span></div>
  <div class="item"><svg width="13" height="10" viewBox="0 0 13 10"><path d="M0 0h13v10H0z M0 0l6.5 5L13 0" /></svg>hello@sparrowgate-petals.com</div>
  <div class="item"><svg width="11" height="11" viewBox="0 0 24 24"><path d="M6.6 10.8a15.1 15.1 0 006.6 6.6l2.2-2.2c.3-.3.7-.4 1-.2 1.1.4 2.3.6 3.6.6.6 0 1 .4 1 1V20c0 .6-.4 1-1 1A17 17 0 013 4c0-.6.4-1 1-1h3.5c.6 0 1 .4 1 1 0 1.3.2 2.5.6 3.6.1.3 0 .7-.2 1z"/></svg>+1-555-014-2287</div>
</div>
<div class="abs brand" style="left:148px;top:44px"><span class="dot"></span><span class="name">Sparrowgate Petals</span></div>
<nav class="nav">
  <a style="left:429px">HOME</a>
  <a style="left:521px">ABOUT</a>
  <a style="left:622px">FOR SUPERMARKETS</a>
  <a style="left:814px">FOR FRANCHISEES</a>
  <a style="left:989px">CONTACT</a>
</nav>

<!-- hero -->
<section class="abs hero" role="img" aria-label="Sunny meadow of wildflowers with daisies and red poppies under a blue sky"></section>
<h1 class="abs script hero-title">Sparrowgate-petals</h1>
<p class="abs hero-text">Fresh flowers convey beauty and love, and in our view should become something every person regularly enjoys.</p>
<a class="btn" style="left:143px;top:341px;width:176px;height:48px;padding-left:34px;font-size:15px">Get Started <svg width="14" height="14" viewBox="0 0 16 16"><circle cx="8" cy="8" r="8"/><path d="M6 4l4 4-4 4" stroke="#f09c20" stroke-width="2" fill="none"/></svg></a>
<svg class="abs" style="left:0;top:600px" width="1200" height="130" viewBox="0 0 1200 130">
  <path d="M0 90 Q260 0 540 84 Q860 145 1200 60 L1200 130 L0 130 Z" fill="#ffffff"/>
  <path d="M0 90 Q260 0 540 84 Q280 22 0 72 Z" fill="#0b8a3e"/>
  <path d="M540 84 Q860 145 1200 60 L1200 40 Q860 138 560 78 Z" fill="#f09c20"/>
</svg>

<!-- about -->
<div class="abs" style="left:112px;top:1026px;width:200px;height:177px;background:var(--green);border-radius:0 0 0 34px"></div>
<div class="abs photo" style="left:130px;top:762px;width:408px;height:417px;border-radius:30px 0 30px 0" role="img" aria-label="Smiling florist holding a potted lavender plant and a basket of fresh produce at a market"></div>
<h2 class="abs script title" style="left:607px;top:778px">About Us</h2>
<div class="abs rule" style="left:608px;top:836px;width:68px"></div>
<div class="abs para" style="left:606px;top:863px;width:448px">
  <p>Fresh flowers convey beauty and love, and in our view should become something every person regularly enjoys.</p>
  <p>Sparrowgate Petals is an entrepreneurial company created to make top quality fresh flowers and professionally-designed bouquets accessible to every consumer at affordable prices.</p>
  <p>Professional florists typically sell the finest quality stems, design the most beautiful bouquets and provide the finest customer service, but their costs – of floral products, retail spaces, labor and marketing – force them to pass high prices along to customers.</p>
</div>
<a class="btn" style="left:606px;top:1117px;width:149px;height:43px;padding-left:25px;font-size:15px">Learn More <svg width="13" height="13" viewBox="0 0 16 16"><circle cx="8" cy="8" r="8"/><path d="M6 4l4 4-4 4" stroke="#f09c20" stroke-width="2" fill="none"/></svg></a>
<div class="abs ornament" style="left:1100px;top:1120px;width:120px;height:130px" role="img" aria-label="Faint line drawing of a rose"></div>

<!-- supermarkets -->
<svg class="abs" style="left:0;top:1306px" width="1200" height="466" viewBox="0 0 1200 466"><path d="M1018 0 H1200 V466 H760 Z" fill="#f09c20"/></svg>
<h2 class="abs script title" style="left:143px;top:1327px">For Supermarkets</h2>
<div class="abs rule" style="left:145px;top:1385px"></div>
<div class="abs para" style="left:144px;top:1411px;width:425px">
  <p>Sparrowgate Petals works with some of the country’s largest and most progressive supermarkets to provide franchisee ownership and operation of their strategically important floral departments. Supermarkets find that Sparrowgate Petals is able to improve their financial outcomes, provide attentive customer service and satisfaction, and lift the quality of the entire store environment.</p>
</div>
<div class="abs subhead" style="left:144px;top:1567px">Opportunity for Supermarkets:</div>
<ul class="abs ticks" style="left:144px;top:1590px">
  <li><svg width="10" height="10" viewBox="0 0 10 10"><circle cx="5" cy="5" r="5" fill="#f09c20"/><path d="M2.8 5.2l1.5 1.4 2.9-3" stroke="#fff" stroke-width="1.3" fill="none"/></svg>Enhance floral revenue streams with efficient assortments and new offerings</li>
  <li><svg width="10" height="10" viewBox="0 0 10 10"><circle cx="5" cy="5" r="5" fill="#f09c20"/><path d="M2.8 5.2l1.5 1.4 2.9-3" stroke="#fff" stroke-width="1.3" fill="none"/></svg>Reduce the costs of operating a floral department</li>
  <li><svg width="10" height="10" viewBox="0 0 10 10"><circle cx="5" cy="5" r="5" fill="#f09c20"/><path d="M2.8 5.2l1.5 1.4 2.9-3" stroke="#fff" stroke-width="1.3" fill="none"/></svg>Maintain a beautiful, fresh and well-stocked environment</li>
</ul>
<a class="btn" style="left:144px;top:1701px;width:148px;height:42px;padding-left:25px;font-size:15px">Learn More <svg width="13" height="13" viewBox="0 0 16 16"><circle cx="8" cy="8" r="8"/><path d="M6 4l4 4-4 4" stroke="#f09c20" stroke-width="2" fill="none"/></svg></a>
<div class="abs ornament" style="left:0;top:1660px;width:120px;height:120px" role="img" aria-label="Faint line drawing of roses"></div>
<div class="abs" style="left:648px;top:1339px;width:428px;height:398px;background:var(--white);border-radius:0 4px 0 4px"></div>
<div class="abs photo" style="left:651px;top:1342px;width:422px;height:392px;background:linear-gradient(160deg,#c9c4a0,#7a8a4c 45%,#e8c43a 80%,#e07a1c)" role="img" aria-label="Smiling gardener in a straw hat holding potted yellow and orange flowers in a greenhouse"></div>

<!-- franchisees -->
<svg class="abs" style="left:0;top:1826px" width="440" height="466" viewBox="0 0 440 466"><path d="M0 0 H172 L437 466 H0 Z" fill="#0b8a3e"/></svg>
<div class="abs" style="left:118px;top:1856px;width:430px;height:401px;background:var(--white)"></div>
<div class="abs photo" style="left:122px;top:1860px;width:423px;height:394px;background:linear-gradient(160deg,#cfd6d0,#8ab08a 40%,#d98aa0 70%,#3a8f7a)" role="img" aria-label="Smiling senior florist in an apron with arms crossed in a flower shop full of bouquets"></div>
<h2 class="abs script title" style="left:629px;top:1857px">For Franchisees</h2>
<div class="abs rule" style="left:632px;top:1915px"></div>
<div class="abs para" style="left:630px;top:1941px;width:424px">
  <p>Sparrowgate Petals brings the best of professional florists and supermarkets together for the benefit of consumers.</p>
  <p>&nbsp;It supports a national network of owner-operator franchisees, who in many cases are multi-site professional florists, with comprehensive services to enhance franchise profitability.</p>
</div>
<div class="abs subhead" style="left:630px;top:2078px">Opportunity for New Florist Franchisees</div>
<ul class="abs ticks" style="left:630px;top:2102px">
  <li><svg width="10" height="10" viewBox="0 0 10 10"><circle cx="5" cy="5" r="5" fill="#f09c20"/><path d="M2.8 5.2l1.5 1.4 2.9-3" stroke="#fff" stroke-width="1.3" fill="none"/></svg>Be an owner, and your own boss</li>
  <li><svg width="10" height="10" viewBox="0 0 10 10"><circle cx="5" cy="5" r="5" fill="#f09c20"/><path d="M2.8 5.2l1.5 1.4 2.9-3" stroke="#fff" stroke-width="1.3" fill="none"/></svg>Attractive earnings potential; paid weekly</li>
  <li><svg width="10" height="10" viewBox="0 0 10 10"><circle cx="5" cy="5" r="5" fill="#f09c20"/><path d="M2.8 5.2l1.5 1.4 2.9-3" stroke="#fff" stroke-width="1.3" fill="none"/></svg>Affordable franchise fees and low initial investment</li>
</ul>
<a class="btn" style="left:630px;top:2210px;width:148px;height:42px;padding-left:25px;font-size:15px">Learn More <svg width="13" height="13" viewBox="0 0 16 16"><circle cx="8" cy="8" r="8"/><path d="M6 4l4 4-4 4" stroke="#f09c20" stroke-width="2" fill="none"/></svg></a>

<!-- footer -->
<svg class="abs" style="left:0;top:2390px" width="1200" height="388" viewBox="0 0 1200 388">
  <path d="M0 110 Q300 0 630 58 Q800 100 930 104 Q1080 98 1200 20 V388 H0 Z" fill="#0e0e0e"/>
  <path d="M0 110 Q300 0 630 58 Q330 20 0 90 Z" fill="#f09c20"/>
  <path d="M663 40 Q800 100 930 104 Q1080 98 1200 20 V8 Q1080 86 930 92 Q800 86 663 40 Z" fill="#0b8a3e"/>
</svg>
<div class="abs brand" style="left:0;top:2538px;width:1200px;justify-content:center"><span class="dot"></span><span class="name" style="font-size:26px">Sparrowgate Petals</span></div>
<div class="abs footer-contact">
  <span class="ci"><svg width="12" height="12" viewBox="0 0 24 24"><path d="M6.6 10.8a15.1 15.1 0 006.6 6.6l2.2-2.2c.3-.3.7-.4 1-.2 1.1.4 2.3.6 3.6.6.6 0 1 .4 1 1V20c0 .6-.4 1-1 1A17 17 0 013 4c0-.6.4-1 1-1h3.5c.6 0 1 .4 1 1 0 1.3.2 2.5.6 3.6.1.3 0 .7-.2 1z"/></svg>+1-555-014-2287</span>
  <span class="sep">|</span>
  <span class="ci"><svg width="10" height="14" viewBox="0 0 10 14"><path d="M5 0a5 5 0 00-5 5c0 4 5 9 5 9s5-5 5-9a5 5 0 00-5-5zm0 7a2 2 0 110-4 2 2 0 010 4z"/></svg>Lorem ipsum dolor sit amet,&nbsp; 40913</span>
  <span class="sep">|</span>
  <span class="ci"><svg width="14" height="11" viewBox="0 0 14 11"><path d="M0 0h14v11H0z"/><path d="M0 0l7 5.5L14 0" stroke="#0e0e0e" stroke-width="1.3" fill="none"/></svg>hello@sparrowgate-petals.com</span>
</div>
<div class="abs divider" style="top:2654px"></div>
<nav class="abs footer-nav">
  <span>HOME</span><span>/</span><span>ABOUT</span><span>/</span><span>FOR SUPERMARKETS</span><span>/</span><span>FOR FRANCHISEES</span><span>/</span><span>CONTACT</span>
</nav>
<div class="abs divider" style="top:2718px"></div>
<p class="abs copyright">Copyright © 2024 Sparrowgate-Petals. All Rights Reserved.</p>

</body>
</html>
```